Briar Crest personal care products line

I need a label design for a line of shampoo, conditioner, beard oil, body butter, massage oil, all containing Hemp oil, All Natural product. No phosphates,
I want the design to feel unisex but want to keep it clean as possible. This is for upscale salons and needs to say on the label professional styling products on the label. Please visit my facebook page www.plumvale.net/briarcrest to see the description of the product benefits. I am attaching some ideas I like as well as the briar crest logo. I would like to see any color of bottle you best think will suit this product as well as new logo design. I am not set on any of these elements. Just the name Briar Crest.
Updates

Project Deadline Extended Reason: I have extended the deadline as I had not filled out the description for the design as it should be. I have also added some features that will define the idea as to what we need. I am open to any desing using Briar Crest. The tag line is not anything I am determined to keep either. Please just be creative and help come up with a great product label for this name and product.Thank you to all ! Added Tuesday, June 2, 2015

Target Market(s)

Salons and upper end market

Industry/Entity Type

Cosmetology

Font styles to use
Serif
Sans Serif

Requirements
Must have
• Logo
Nice to have
• Bottle and packaging ideas on color and shape of bottle

```html
<!DOCTYPE html>
<html lang="en">
<head>
<meta charset="utf-8">
<title>Briar Crest Body Butter Label</title>
<link href="https://fonts.googleapis.com/css2?family=Andada+Pro:ital,wght@1,400&family=Delius&family=Lato:wght@300;400&display=swap" rel="stylesheet">
<style>
  :root {
    --berry: #9b2066;
    --berry-dark: #80124f;
    --leaf: #3cb54a;
    --ink: #575757;
    --paper: #ffffff;
  }
  html, body {
    margin: 0;
    padding: 0;
    overflow: hidden;
    background: var(--paper);
  }
  .label {
    position: relative;
    width: 1200px;
    height: 208px;
    background: var(--paper);
    overflow: hidden;
  }
  .band {
    position: absolute;
    left: 0;
    width: 100%;
    height: 20px;
    background: linear-gradient(to bottom, var(--berry-dark), var(--berry) 45%, var(--berry-dark));
  }
  .band--top { top: 0; }
  .band--bottom { bottom: 0; height: 21px; }

  .claim {
    position: absolute;
    left: 67px;
    top: 57px;
    width: 240px;
    margin: 0;
    text-align: center;
    font-family: "Andada Pro", Georgia, serif;
    font-style: italic;
    font-size: 13.5px;
    line-height: 21px;
    color: var(--ink);
  }
  .website {
    position: absolute;
    left: 67px;
    top: 169px;
    width: 240px;
    margin: 0;
    text-align: center;
    font-family: "Lato", "Gill Sans", sans-serif;
    font-weight: 400;
    font-size: 13px;
    color: var(--ink);
    letter-spacing: 0.2px;
  }
  .brand-mark {
    position: absolute;
    left: 518px;
    top: 52px;
    width: 106px;
    height: 106px;
  }
  .brand-name {
    position: absolute;
    left: 646px;
    top: 26px;
    margin: 0;
    font-family: "Lato", "Gill Sans", sans-serif;
    font-weight: 400;
    font-size: 44px;
    line-height: 50px;
    letter-spacing: 5px;
    color: var(--berry);
    white-space: nowrap;
  }
  .line-name {
    position: absolute;
    left: 721px;
    top: 80px;
    margin: 0;
    font-family: "Lato", "Gill Sans", sans-serif;
    font-weight: 300;
    font-size: 16px;
    color: var(--ink);
    white-space: nowrap;
  }
  .product {
    position: absolute;
    left: 680px;
    top: 124px;
    width: 300px;
    margin: 0;
    text-align: center;
    font-family: "Delius", "Trebuchet MS", sans-serif;
    font-size: 25px;
    color: var(--leaf);
  }
  .volume {
    position: absolute;
    left: 720px;
    top: 168px;
    width: 200px;
    margin: 0;
    text-align: center;
    font-family: "Lato", "Gill Sans", sans-serif;
    font-weight: 400;
    font-size: 10px;
    color: var(--ink);
    word-spacing: 2px;
  }
</style>
</head>
<body>
  <main class="label">
    <div class="band band--top"></div>

    <p class="claim">100% natural hair &amp; Scalp nourishment with Acedic Acid &amp; Hemp Omega 3 Oils.</p>
    <p class="website">WWW.BRIARCRESTINC.COM</p>

    <svg class="brand-mark" viewBox="0 0 106 106" aria-hidden="true">
      <circle cx="53" cy="53" r="50" fill="var(--leaf)"/>
    </svg>
    <h1 class="brand-name">BRIAR CREST</h1>
    <p class="line-name">Professional Styling Products</p>

    <h2 class="product">Body Butter</h2>
    <p class="volume">8 fl. oz.&nbsp;&nbsp; 237 ml.</p>

    <div class="band band--bottom"></div>
  </main>
</body>
</html>
```